Dietitian needs awesome business card

I need a contemporary design that's eye catching but professional.
My card is to given to doctors, specialists and patients alike.
I manage patients with chronic diseases
I have uploaded my logo and current business card, I would also like the other Registered Clinical Nutritionist logo incorporated into the design

Target Market(s)

Doctors, specialists and patients

Industry/Entity Type

Healthcare

Contact Information for Business Card

www.brindlecovenutrition.com.au
Ph: 0427 516 903
Fax: 6482 7315
email: marcus.k.wellfare@quorvamail.com
Space on the back of the card with: Appointment date, Appointment time and appointment location

Font styles to use
Serif

Colors
fbee3e
876aae
ffc214

Requirements
Must have
• My Logo
• Registered Clinical Nutritionist Logo
• My 4 locations - Fernhollow Medical Centre, North Kelby Health, Ashcourt Medical, Pinebrook Doctors Surgery
Nice to have
• I like the colours in my current business card

```html
<!DOCTYPE html>
<html lang="en">
<head>
<meta charset="utf-8">
<title>Brindlecove Nutrition &amp; Dietetics – Business Card</title>
<link rel="stylesheet" href="https://fonts.googleapis.com/css2?family=Tinos:wght@400;700&family=Quicksand:wght@500;600&family=Open+Sans:wght@600&family=Didact+Gothic&display=swap">
<style>
  :root{
    --stage:#353c3c;
    --paper:#ffffff;
    --brand-blue:#2f6fdc;
    --deep-blue:#1f3fc4;
    --lime:#8fd329;
    --orange:#fb5a0a;
    --faint-blue:#e6e9fb;
    --faint-green:#f1f8e4;
  }
  *{margin:0;padding:0;box-sizing:border-box}
  html,body{width:1200px;height:1200px;overflow:hidden;background:var(--stage)}
  .stage{position:relative;width:1200px;height:1200px}
  .card{position:absolute;left:165px;width:898px;height:518px;background:var(--paper);overflow:hidden}
  .card--front{top:61px}
  .card--back{top:606px}
  .card svg.backdrop{position:absolute;inset:0;width:100%;height:100%}
  .abs{position:absolute;white-space:nowrap}

  /* front */
  .brand-dot{left:27px;top:75px;width:136px;height:136px;border-radius:50%;background:var(--brand-blue)}
  .brand-name{left:178px;top:128px;font-family:"Tinos",serif;font-weight:400;color:var(--deep-blue);line-height:1}
  .brand-name .main{display:block;font-size:54px}
  .brand-name .sub{display:block;font-size:25px;margin-top:6px;margin-left:6px}
  .person{left:42px;top:260px;font-family:"Tinos",serif;font-weight:700;font-size:32px;letter-spacing:9px;color:var(--brand-blue)}
  .contact{left:42px;color:#fff;font-size:24px}
  .contact .label{font-family:"Tinos",serif}
  .contact .value{font-family:"Quicksand",sans-serif;font-weight:600}
  .contact--tel{top:321px}
  .contact--fax{top:361px;left:46px}
  .contact--mail{top:404px;left:46px;font-size:21px}
  .web{left:44px;top:470px;font-family:"Quicksand",sans-serif;font-weight:600;font-size:23px;color:var(--brand-blue)}
  .credential{left:600px;top:52px;font-family:"Open Sans",sans-serif;font-weight:600;font-size:22px;line-height:28px;color:#fff}
  .badge{left:760px;top:35px;width:116px;height:116px;border-radius:50%;background:#fff}

  /* back */
  .top-rule{left:0;top:0;width:100%;height:7px;background:var(--lime)}
  .title{left:0;width:100%;top:20px;text-align:center;font-family:"Didact Gothic",sans-serif;font-size:58px;letter-spacing:5px;color:var(--brand-blue)}
  .watermark-dot{left:27px;top:162px;width:240px;height:240px;border-radius:50%;background:var(--faint-blue);opacity:.7}
  .watermark-name{left:290px;top:218px;font-family:"Tinos",serif;font-size:84px;color:var(--faint-blue);line-height:1}
  .field{font-family:"Didact Gothic",sans-serif;font-size:28px;color:var(--brand-blue)}
  .field-line{height:1px;background:var(--brand-blue);opacity:.8}
  .footer-band{left:0;bottom:0;width:100%;height:45px;background:var(--brand-blue);color:#fff;text-align:center;font-family:"Quicksand",sans-serif;font-weight:600;font-size:26px;letter-spacing:2px;line-height:45px}
</style>
</head>
<body>
<main class="stage">

  <section class="card card--front">
    <svg class="backdrop" viewBox="0 0 898 518" preserveAspectRatio="none" aria-hidden="true">
      <rect class="contact-band" x="0" y="312" width="640" height="134" fill="var(--lime)"/>
      <path d="M536,0 C510,100 600,200 590,315 C580,410 520,480 452,518 L898,518 L898,0 Z" fill="var(--lime)"/>
      <path d="M562,0 C536,100 626,200 616,315 C606,410 556,480 494,518 L898,518 L898,0 Z" fill="var(--brand-blue)"/>
      <path d="M594,0 C566,100 646,200 638,315 C630,410 586,480 530,518 L898,518 L898,0 Z" fill="var(--orange)"/>
    </svg>

    <div class="abs brand-dot"></div>
    <div class="abs brand-name">
      <span class="main">Brindlecove</span>
      <span class="sub">Nutrition &amp; Dietetics</span>
    </div>

    <div class="abs person">Marcus Kellaway</div>

    <div class="abs contact contact--tel"><span class="label">Tel:</span> <span class="value">0427 516 903</span></div>
    <div class="abs contact contact--fax"><span class="label">Fax:</span> <span class="value">6482 7315</span></div>
    <div class="abs contact contact--mail"><span class="label">Email:</span> <span class="value">marcus.k.wellfare@quorvamail.com</span></div>

    <div class="abs web">www.brindlecovenutrition.com.au</div>

    <div class="abs credential">Registered<br>Clinical<br>Nutritionist</div>
    <div class="abs badge"></div>
  </section>

  <section class="card card--back">
    <div class="abs top-rule"></div>
    <div class="abs watermark-dot"></div>
    <div class="abs watermark-name">Brindlecove</div>

    <h1 class="abs title">APPOINTMENT</h1>

    <div class="abs field" style="left:70px;top:116px">Date</div>
    <div class="abs field-line" style="left:153px;top:144px;width:685px"></div>

    <div class="abs field" style="left:66px;top:248px">Time</div>
    <div class="abs field-line" style="left:163px;top:274px;width:675px"></div>

    <div class="abs field" style="left:66px;top:376px">Location</div>
    <div class="abs field-line" style="left:201px;top:404px;width:637px"></div>

    <div class="abs footer-band">Dietitian, Nutritionist and Chef</div>
  </section>

</main>
</body>
</html>
```